Electrical panel service sticker w Bucket truck & Logo

We have a rather plain sticker we put on lighting panels to remind customers who to call for service. We want to redesign them with brushed aluminum background. We want a remake of the sticker with the outline of a bucket truck. You'll need to find or draw the outling of a bucket truck maybe with the boom up slightly as we will get these stickers die cut.

We want LOGO with Ph.# and Email.
Electrical * Lighting * Sign Service

Target Market(s)

Commercial property managers

Industry/Entity Type

Property Management

Requirements
Must have
• Bucket Truck Outline

```html
<!DOCTYPE html>
<html lang="en">
<head>
<meta charset="utf-8">
<title>Panel Service Sticker</title>
<link rel="stylesheet" href="https://fonts.googleapis.com/css2?family=Barlow+Condensed:wght@500;600;700&display=swap">
<style>
  :root {
    --page-bg: #ececec;
    --alu-light: #d6d6d6;
    --alu-mid: #bdbdbd;
    --alu-dark: #a9a9a9;
    --ink: #141414;
    --panel-black: #000000;
    --panel-text: #b9b9b9;
    --accent-tone: #3a3a3a;
  }
  * { margin: 0; padding: 0; box-sizing: border-box; }
  html, body {
    width: 1200px; height: 1200px; overflow: hidden;
    background: var(--page-bg);
  }
  .sticker {
    position: absolute; left: 77px; top: 286px;
    width: 1045px; height: 626px;
    display: flex;
    font-family: "Barlow Condensed", "Arial Narrow", sans-serif;
  }
  .contact-side {
    position: relative; width: 583px; height: 100%;
    background:
      repeating-linear-gradient(0deg, rgba(255,255,255,0.10) 0 1px, rgba(0,0,0,0.04) 1px 2px, transparent 2px 3px),
      linear-gradient(100deg, var(--alu-dark) 0%, var(--alu-light) 40%, var(--alu-mid) 70%, var(--alu-light) 100%);
    color: var(--ink);
    text-align: center;
  }
  .truck-art {
    position: absolute; left: 89px; top: 64px;
    width: 386px; height: 219px;
    background: linear-gradient(180deg, rgba(143,143,143,0.55), rgba(120,120,120,0.55));
    border-radius: 6px;
  }
  .call-label {
    position: absolute; left: 0; right: 0; top: 335px;
    font-size: 68px; font-weight: 700; letter-spacing: 1px; line-height: 1;
  }
  .phone {
    position: absolute; left: 0; right: 0; top: 414px;
    font-size: 98px; font-weight: 700; line-height: 1;
  }
  .email {
    position: absolute; left: 0; right: 0; top: 527px;
    font-size: 38px; font-weight: 600; line-height: 1;
  }
  .services-side {
    position: relative; flex: 1; height: 100%;
    background: var(--panel-black);
  }
  .list-accent {
    position: absolute; left: 0; top: 208px;
    width: 59px; height: 200px;
    background: linear-gradient(90deg, var(--accent-tone), #2a2a2a);
  }
  .service-list { list-style: none; }
  .service-list li {
    position: absolute; left: 115px;
    font-size: 60px; font-weight: 500; letter-spacing: 1.5px;
    color: var(--panel-text); line-height: 1;
    white-space: nowrap;
    transform: translateY(-50%);
  }
  .service-list li:nth-child(1) { top: 233px; }
  .service-list li:nth-child(2) { top: 311px; }
  .service-list li:nth-child(3) { top: 390px; }
</style>
</head>
<body>
  <div class="sticker">
    <section class="contact-side">
      <div class="truck-art" role="img" aria-label="Outline drawing of a bucket truck with its boom raised"></div>
      <p class="call-label">FOR SERVICE CALL</p>
      <p class="phone">800-555-0148</p>
      <p class="email">Service@BrightlinePanelCare.com</p>
    </section>
    <section class="services-side">
      <div class="list-accent" role="img" aria-label="Decorative tube accents beside the service list"></div>
      <ul class="service-list">
        <li>ELECTRICAL</li>
        <li>LIGHTING</li>
        <li>SIGN SERVICE</li>
      </ul>
    </section>
  </div>
</body>
</html>
```